Norwegian language blog www.lumadio.com / www.lumadio.no

I want to make a blog where I share my thoughts and ideas about Norwegian language. I already have a YouTube channel with almost 40000 followers and a podcast with more than 10000 listeners, so this blog will be the extention of those channels. In addition I have my own online school, check www.vilpa.noI have a logo and everything, so I just need a fresh vibrant blog to go with my concept. I want to keep the colors in my logo and also add my logo of course. Then the blog should be easy to read. I need some pictures of the Norwegian flag or something.I want a fun and cool design.
Check my youtube here: https://www.videohub.example/channel/UCxqWPT415mKaZ8Lf2dHoRwn?view_as=subscriber
Website here: www.vilpa.no

The blog will be for my new domain www.lumadio.no and I also have the same domain with www.lumadio.com - I want to put them both in one URL, like when you write www.lumadio.no or .com you will reach the same page.

Target Market(s)

Student who want to learn Norwegian and learn about Norwegian culture

Industry/Entity Type

Education

Coding

Coded - Design and coding required

Number of Pages Required

1 page

Font styles to use
Sans Serif

Colors
e34398
00a990
f78f20
0492cd
86cfc6
85cae6
f8ba93
eda3c7
ffc214

Requirements
Must have
• The colors of my logo, check www.vilpa.no
• Cool and elegant layout
• Pictures of Norway
• Picture of me
• Picture of the Norwegian flag
Should not have
• too many colors and pictures of random people

```html
<!DOCTYPE html>
<html lang="en">
<head>
<meta charset="utf-8">
<title>Vilpa – Norwegian language blog</title>
<link href="https://fonts.googleapis.com/css2?family=Open+Sans:wght@400;600;700&family=Raleway:wght@400;600&display=swap" rel="stylesheet">
<style>
:root{
  --pink:#e34398;
  --green:#00a990;
  --orange:#f78f20;
  --blue:#0492cd;
  --mint:#86cfc6;
  --sky:#85cae6;
  --peach:#f8ba93;
  --rose:#eda3c7;
  --yellow:#ffc214;
  --ink:#2f2f2f;
  --text:#6b6b6b;
  --muted:#9a9a9a;
  --line:#e4e4e4;
  --footer:#f4f4f4;
  --bar:#2a2a2a;
}
*{box-sizing:border-box;margin:0;padding:0}
html,body{width:1200px;height:3820px;overflow:hidden;background:#fff}
body{font-family:"Open Sans",Arial,sans-serif;color:var(--text);position:relative}
a{color:inherit;text-decoration:none}
ul{list-style:none}

.hero{position:absolute;left:0;top:0;width:1200px;height:652px;
  background:linear-gradient(100deg,#e9e4dc 0%,#f4efe7 30%,#d8c3a8 52%,#7a5a45 70%,#c9a58a 85%,#efe6da 100%)}
.brand{position:absolute;left:78px;top:26px;display:flex;align-items:center;gap:12px}
.brand-dot{width:46px;height:46px;border-radius:50%;background:var(--pink)}
.brand-name{font-size:34px;font-weight:600;color:#3a3a3a}

.posts{position:absolute;left:73px;top:700px;width:694px;display:grid;
  grid-template-columns:334px 334px;column-gap:26px;grid-auto-rows:533px}
.post-thumb{height:255px;width:100%}
.post-title{font-size:21px;font-weight:400;color:var(--ink);line-height:1.3;margin-top:12px}
.post-excerpt{font-size:14px;line-height:1.55;margin-top:10px;color:var(--text)}
.post-meta{font-size:12px;color:var(--muted);margin-top:14px;display:flex;gap:16px;align-items:center}
.post-meta svg{vertical-align:-2px;margin-right:5px}

.sidebar{position:absolute;left:792px;top:700px;width:335px}
.search{height:44px;border:1px solid var(--line);display:flex;align-items:center;justify-content:space-between;padding:0 14px;font-size:13px;color:#b5b5b5}
.widget-title{font-size:15px;font-weight:600;color:var(--ink);text-align:center;text-transform:uppercase;letter-spacing:.5px;padding-bottom:10px;position:relative}
.widget-title::after{content:"";position:absolute;left:50%;bottom:0;width:44px;height:2px;margin-left:-22px;background:var(--pink)}
.widget-title.plain{text-transform:none}
.about{margin-top:34px}
.author-photo{height:255px;margin-top:16px;background:linear-gradient(135deg,#dfe7ee,#c9d4de 55%,#b8443d 56%,#d9d9e6 80%)}
.about-text{font-size:14px;line-height:1.55;margin-top:14px}
.read-more{display:block;color:var(--blue);font-size:14px;margin-top:16px;text-decoration:underline}
.signature{width:80px;height:40px;margin-top:14px;background:linear-gradient(90deg,#e9e9e9,#d0d0d0)}
.box{border:1px solid var(--line);padding:18px 20px}
.follow{margin-top:26px;height:143px}
.social{display:flex;justify-content:center;gap:10px;margin-top:18px}
.social span{width:16px;height:16px;border-radius:50%;background:#555}
.archives{margin-top:12px}
.archives li,.tags li{font-size:14px;display:flex;justify-content:space-between;padding:12px 0;border-bottom:1px solid #f0f0f0}
.archives li:last-child,.tags li:last-child{border-bottom:0}
.archives ul,.tags ul{margin-top:14px}
.tags{margin-top:12px}
.tags li{padding:11px 0}
.recent{margin-top:32px}
.recent ul{margin-top:18px}
.recent li{display:flex;gap:12px;height:125px}
.recent-thumb{width:95px;height:88px;flex:none}
.recent-title{font-size:14px;color:var(--ink);line-height:1.35}
.recent-meta{font-size:11px;color:var(--muted);margin-top:4px}
.subscribe{margin-top:8px;padding-bottom:20px}
.field{height:40px;border:1px solid var(--line);margin-top:14px;font-size:12px;color:#b5b5b5;padding:11px 12px}
.field+.field{margin-top:10px}
.btn{height:38px;margin-top:10px;background:var(--pink);color:#fff;font-size:13px;text-align:center;line-height:38px}

.pager{position:absolute;left:73px;top:3408px;font-size:15px;display:flex;gap:12px;align-items:center;color:var(--text)}
.pager .current{color:var(--pink)}

.footer{position:absolute;left:0;top:3470px;width:1200px;height:300px;background:var(--footer)}
.foot-col{position:absolute;top:22px}
.foot-title{font-size:16px;color:var(--ink);padding-bottom:8px;border-bottom:1px solid #ddd;margin-bottom:12px}
.foot-about{left:84px;width:230px;font-size:13px;line-height:1.55;color:var(--pink)}
.foot-about .more{color:var(--pink);font-weight:600}
.foot-posts{left:440px;width:300px}
.foot-posts li{display:flex;gap:10px;margin-bottom:14px}
.foot-posts .mini{width:45px;height:40px;flex:none}
.foot-posts p{font-size:12px;color:var(--ink);line-height:1.35}
.foot-posts small{font-size:10px;color:var(--muted)}
.foot-arch{left:790px;width:80px;font-size:13px}
.foot-arch li{margin-bottom:13px}
.foot-tags{left:880px;width:250px}
.foot-tags ul{display:flex;flex-wrap:wrap;gap:8px}
.foot-tags li{border:1px solid #cfcfcf;font-size:12px;padding:3px 7px;background:#fff}
.bottom{position:absolute;left:0;top:3770px;width:1200px;height:50px;background:var(--bar);color:#9d9d9d;font-size:12px;padding:17px 84px}
</style>
</head>
<body>

<header class="hero" role="img" aria-label="Photo of two women studying together at a laptop in a bright room">
  <div class="brand"><span class="brand-dot"></span><span class="brand-name">Vilpa</span></div>
</header>

<main class="posts">
  <article class="post">
    <div class="post-thumb" role="img" aria-label="Teacher holding a card with a Norwegian word" style="background:linear-gradient(135deg,#e6d8cc,#c9a892 60%,#f1ede6)"></div>
    <h2 class="post-title">Online education through our platform!</h2>
    <p class="post-excerpt">Online tuition is a great opportunity to learn Norwegian from home! All lessons are tailored to your needs and the teaching time is very flexible.</p>
    <div class="post-meta"><span><svg width="11" height="11" viewBox="0 0 11 11"><rect x=".5" y="1.5" width="10" height="9" fill="none" stroke="#999"/><line x1="0" y1="4" x2="11" y2="4" stroke="#999"/></svg>Posted on 05th Dec 2018</span><span><svg width="10" height="11" viewBox="0 0 10 11"><circle cx="5" cy="3" r="2.5" fill="#999"/><path d="M0 11a5 5 0 0 1 10 0z" fill="#999"/></svg>By Lunea</span></div>
  </article>
  <article class="post">
    <div class="post-thumb" role="img" aria-label="Teacher speaking to camera in a pink top" style="background:linear-gradient(135deg,#d9c9c4,#c48aa0 55%,#ece3e2)"></div>
    <h2 class="post-title">We do not speak English and Norwegian</h2>
    <p class="post-excerpt">Having been outside a winter night before – you have many experiences in life, also tough hesitations Contact: hello@vilpa.no</p>
    <div class="post-meta"><span><svg width="11" height="11" viewBox="0 0 11 11"><rect x=".5" y="1.5" width="10" height="9" fill="none" stroke="#999"/><line x1="0" y1="4" x2="11" y2="4" stroke="#999"/></svg>Posted on 05th Dec 2018</span><span><svg width="10" height="11" viewBox="0 0 10 11"><circle cx="5" cy="3" r="2.5" fill="#999"/><path d="M0 11a5 5 0 0 1 10 0z" fill="#999"/></svg>By Lunea</span></div>
  </article>
  <article class="post">
    <div class="post-thumb" role="img" aria-label="Chess pieces on a board" style="background:linear-gradient(135deg,#5a4632,#a08060 50%,#2c2219)"></div>
    <h2 class="post-title">Riga, chessmaster Henrik Alstad, training and music</h2>
    <p class="post-excerpt">I'm telling you about the trip to Riga. It's important to stay in good shape, too mentally! When I was a child I played chess and I have many nice memories from that time.</p>
    <div class="post-meta"><span><svg width="11" height="11" viewBox="0 0 11 11"><rect x=".5" y="1.5" width="10" height="9" fill="none" stroke="#999"/><line x1="0" y1="4" x2="11" y2="4" stroke="#999"/></svg>Posted on 05th Dec 2018</span><span><svg width="10" height="11" viewBox="0 0 10 11"><circle cx="5" cy="3" r="2.5" fill="#999"/><path d="M0 11a5 5 0 0 1 10 0z" fill="#999"/></svg>By Lunea</span></div>
  </article>
  <article class="post">
    <div class="post-thumb" role="img" aria-label="White Norwegian house under a blue sky" style="background:linear-gradient(180deg,#a9c4de,#dfe6ec 45%,#8c8a80 75%,#6d6a5e)"></div>
    <h2 class="post-title">Norwegian children's education Housing purchases in Norway</h2>
    <p class="post-excerpt">I tell about childcare in Norway, how parents think and are with their children. It is different to be raised in Norway and I want to teach you how we think about it.</p>
    <div class="post-meta"><span><svg width="11" height="11" viewBox="0 0 11 11"><rect x=".5" y="1.5" width="10" height="9" fill="none" stroke="#999"/><line x1="0" y1="4" x2="11" y2="4" stroke="#999"/></svg>Posted on 05th Dec 2018</span><span><svg width="10" height="11" viewBox="0 0 10 11"><circle cx="5" cy="3" r="2.5" fill="#999"/><path d="M0 11a5 5 0 0 1 10 0z" fill="#999"/></svg>By Lunea</span></div>
  </article>
  <article class="post">
    <div class="post-thumb" role="img" aria-label="Tropical beach with palm trees" style="background:linear-gradient(180deg,#4fb3e4,#9fdcef 45%,#48c0b8 60%,#f0e2b8)"></div>
    <h2 class="post-title">Summer Podcast! England, Turkey and the Netherlands</h2>
    <p class="post-excerpt">Summer greetings to all of you! This podcast I have made in Turkey. I tell about my summer in Norway and abroad. Hope you all are fine!</p>
    <div class="post-meta"><span><svg width="11" height="11" viewBox="0 0 11 11"><rect x=".5" y="1.5" width="10" height="9" fill="none" stroke="#999"/><line x1="0" y1="4" x2="11" y2="4" stroke="#999"/></svg>Posted on 05th Dec 2018</span><span><svg width="10" height="11" viewBox="0 0 10 11"><circle cx="5" cy="3" r="2.5" fill="#999"/><path d="M0 11a5 5 0 0 1 10 0z" fill="#999"/></svg>By Lunea</span></div>
  </article>
  <article class="post">
    <div class="post-thumb" role="img" aria-label="Teacher holding a card with the idiom of the week" style="background:linear-gradient(135deg,#dcd0c4,#b78f72 55%,#efe9e1)"></div>
    <h2 class="post-title">Idiom number 76 Hybelkanin</h2>
    <p class="post-excerpt">An idiom is a phrase, saying or a group of words that has a metaphorical (not literal) meaning, which has become accepted in common usage.</p>
    <div class="post-meta"><span><svg width="11" height="11" viewBox="0 0 11 11"><rect x=".5" y="1.5" width="10" height="9" fill="none" stroke="#999"/><line x1="0" y1="4" x2="11" y2="4" stroke="#999"/></svg>Posted on 05th Dec 2018</span><span><svg width="10" height="11" viewBox="0 0 10 11"><circle cx="5" cy="3" r="2.5" fill="#999"/><path d="M0 11a5 5 0 0 1 10 0z" fill="#999"/></svg>By Lunea</span></div>
  </article>
  <article class="post">
    <div class="post-thumb" role="img" aria-label="Book cover about working with Norwegians" style="background:linear-gradient(180deg,#f6f6f6,#e9e9e9 60%,#f3f3f3)"></div>
    <h2 class="post-title">Tax in Norway, Marit Solberg and dental tourism</h2>
    <p class="post-excerpt">We pay a lot of tax in Norway, but I'm telling you a little about why it's like that. Today, I have had a meeting with Marit Solberg who has written the book: "Working Among Norwegians..."</p>
    <div class="post-meta"><span><svg width="11" height="11" viewBox="0 0 11 11"><rect x=".5" y="1.5" width="10" height="9" fill="none" stroke="#999"/><line x1="0" y1="4" x2="11" y2="4" stroke="#999"/></svg>Posted on 05th Dec 2018</span><span><svg width="10" height="11" viewBox="0 0 10 11"><circle cx="5" cy="3" r="2.5" fill="#999"/><path d="M0 11a5 5 0 0 1 10 0z" fill="#999"/></svg>By Lunea</span></div>
  </article>
  <article class="post">
    <div class="post-thumb" role="img" aria-label="Hands decorated with henna for a wedding" style="background:linear-gradient(135deg,#7a3b26,#b86a42 50%,#5a2a1c)"></div>
    <h2 class="post-title">March 8, Pakistani wedding and Norwegians abroad</h2>
    <p class="post-excerpt">I'm talking about Women's Day that was March 8 and what it means to me. I have been to a wedding for my good girlfriend who got married on Saturday.</p>
    <div class="post-meta"><span><svg width="11" height="11" viewBox="0 0 11 11"><rect x=".5" y="1.5" width="10" height="9" fill="none" stroke="#999"/><line x1="0" y1="4" x2="11" y2="4" stroke="#999"/></svg>Posted on 05th Dec 2018</span><span><svg width="10" height="11" viewBox="0 0 10 11"><circle cx="5" cy="3" r="2.5" fill="#999"/><path d="M0 11a5 5 0 0 1 10 0z" fill="#999"/></svg>By Lunea</span></div>
  </article>
  <article class="post">
    <div class="post-thumb" role="img" aria-label="Portrait of the teacher with blonde hair" style="background:linear-gradient(135deg,#e4d6c6,#caa98c 55%,#f0e8de)"></div>
    <h2 class="post-title">Riga, chessmaster Henrik Alstad, training and music</h2>
    <p class="post-excerpt">I'm telling you about the trip to Riga. It's important to stay in good shape, too mentally! When I was a child I played chess and I have many nice memories from that time.</p>
    <div class="post-meta"><span><svg width="11" height="11" viewBox="0 0 11 11"><rect x=".5" y="1.5" width="10" height="9" fill="none" stroke="#999"/><line x1="0" y1="4" x2="11" y2="4" stroke="#999"/></svg>Posted on 05th Dec 2018</span><span><svg width="10" height="11" viewBox="0 0 10 11"><circle cx="5" cy="3" r="2.5" fill="#999"/><path d="M0 11a5 5 0 0 1 10 0z" fill="#999"/></svg>By Lunea</span></div>
  </article>
  <article class="post">
    <div class="post-thumb" role="img" aria-label="White town by the sea in Oman" style="background:linear-gradient(180deg,#9cc3e0,#d9e3e8 40%,#c9c2b4 70%,#8a8676)"></div>
    <h2 class="post-title">Oman, desert safaris and volunteers in Norway</h2>
    <p class="post-excerpt">I have been to Oman and tell about my trip there. It was a great trip! I also talk about some of what you have asked for on my channel.</p>
    <div class="post-meta"><span><svg width="11" height="11" viewBox="0 0 11 11"><rect x=".5" y="1.5" width="10" height="9" fill="none" stroke="#999"/><line x1="0" y1="4" x2="11" y2="4" stroke="#999"/></svg>Posted on 05th Dec 2018</span><span><svg width="10" height="11" viewBox="0 0 10 11"><circle cx="5" cy="3" r="2.5" fill="#999"/><path d="M0 11a5 5 0 0 1 10 0z" fill="#999"/></svg>By Lunea</span></div>
  </article>
</main>

<aside class="sidebar">
  <div class="search">Search<svg width="14" height="14" viewBox="0 0 14 14"><circle cx="6" cy="6" r="4.5" fill="none" stroke="#bbb" stroke-width="1.5"/><line x1="9.5" y1="9.5" x2="13" y2="13" stroke="#bbb" stroke-width="1.5"/></svg></div>

  <section class="about">
    <h3 class="widget-title">About Author</h3>
    <div class="author-photo" role="img" aria-label="The author holding a Norwegian flag"></div>
    <p class="about-text">For those who want to learn Norwegian quickly from professional teachers.<br>For those who apply for a permanent residence permit and need approved hours and course certificates<br>For those who want to study Norwegian or social knowledge from home<br>You've come to the right place!<br>Vilpa is an online school that offers tailor made teaching for those who wish to learn the Norwegian language. Regardless of whether you live in Norway or abroad, you can get online teaching instructors. We have highly qualified teachers who can help you learn the Norwegian language.</p>
    <a class="read-more" href="#">Read more</a>
    <div class="signature" role="img" aria-label="Author's handwritten signature"></div>
  </section>

  <section class="box follow">
    <h3 class="widget-title">Follow Me</h3>
    <div class="social"><span></span><span></span><span></span><span></span><span></span><span></span></div>
  </section>

  <section class="box archives">
    <h3 class="widget-title">Search the Archives</h3>
    <ul>
      <li><span>December 2018</span><span>(09)</span></li>
      <li><span>November 2018</span><span>(22)</span></li>
      <li><span>October 2018</span><span>(13)</span></li>
      <li><span>September 2018</span><span>(28)</span></li>
    </ul>
  </section>

  <section class="box tags">
    <h3 class="widget-title">Tags</h3>
    <ul>
      <li>Norwegian</li><li>Online course</li><li>Education</li><li>Training</li><li>Study</li>
    </ul>
  </section>

  <section class="recent">
    <h3 class="widget-title">Recent Video &amp; Podcast</h3>
    <ul>
      <li><div class="recent-thumb" role="img" aria-label="Chess pieces" style="background:linear-gradient(135deg,#5a4632,#a08060)"></div><div><p class="recent-title">Riga, chessmaster Henrik Alstad, training and music</p><p class="recent-meta">Podcast &nbsp;05.12.2018</p></div></li>
      <li><div class="recent-thumb" role="img" aria-label="Teacher video still" style="background:linear-gradient(135deg,#d9c9c4,#c48aa0)"></div><div><p class="recent-title">Video 476 We do not speak English and Norwegian</p><p class="recent-meta">Video &nbsp;21.11.2018</p></div></li>
      <li><div class="recent-thumb" role="img" aria-label="Teacher video still" style="background:linear-gradient(135deg,#dce2ea,#a9b6c8)"></div><div><p class="recent-title">Video 482 Advent Calendar 5th of December</p><p class="recent-meta">Video &nbsp;05.12.2018</p></div></li>
      <li><div class="recent-thumb" role="img" aria-label="Teacher video still" style="background:linear-gradient(135deg,#e3d6cb,#b99a82)"></div><div><p class="recent-title">Video 474 Degree bending of adjectives with MER &amp; MEST</p><p class="recent-meta">Video &nbsp;26.11.2018</p></div></li>
      <li><div class="recent-thumb" role="img" aria-label="Beach with palm trees" style="background:linear-gradient(180deg,#4fb3e4,#48c0b8 60%,#f0e2b8)"></div><div><p class="recent-title">Summer Podcast! England, Turkey and the Netherlands</p><p class="recent-meta">Podcast &nbsp;01.01.2018</p></div></li>
    </ul>
  </section>

  <section class="box subscribe">
    <h3 class="widget-title">Subscribe</h3>
    <div class="field">Name</div>
    <div class="field">Enter your mail id</div>
    <div class="btn">FOLLOW</div>
  </section>
</aside>

<nav class="pager"><span class="current">1</span><span>2</span><span>3</span><span>4</span><span>Next</span><svg width="30" height="10" viewBox="0 0 30 10"><line x1="0" y1="5" x2="27" y2="5" stroke="#333" stroke-width="1.5"/><path d="M22 1l6 4-6 4" fill="none" stroke="#333" stroke-width="1.5"/></svg></nav>

<footer class="footer">
  <div class="foot-col foot-about">
    <h4 class="foot-title">About</h4>
    <p>For those who want to learn Norwegian quickly from professional teachers.<br>For those who apply for a permanent residence permit and need approved hours and course certificates <span class="more">more</span></p>
  </div>
  <div class="foot-col foot-posts">
    <h4 class="foot-title">Recent Posts</h4>
    <ul>
      <li><div class="mini" role="img" aria-label="Teacher video still" style="background:linear-gradient(135deg,#dce2ea,#a9b6c8)"></div><div><p>Video 482 Advent Calendar 5th of December</p><small>05.12.2018</small></div></li>
      <li><div class="mini" role="img" aria-label="Henna decorated hands" style="background:linear-gradient(135deg,#7a3b26,#b86a42)"></div><div><p>March 8, Pakistani wedding and Norwegians abroad</p><small>04.12.2018</small></div></li>
      <li><div class="mini" role="img" aria-label="Norwegian house" style="background:linear-gradient(180deg,#a9c4de,#8c8a80)"></div><div><p>Norwegian children's education Housing purchases in Norway</p><small>03.12.2018</small></div></li>
    </ul>
  </div>
  <div class="foot-col foot-arch">
    <h4 class="foot-title">Archives</h4>
    <ul><li>December</li><li>November</li><li>October</li><li>September</li><li>August</li></ul>
  </div>
  <div class="foot-col foot-tags">
    <h4 class="foot-title">Tags</h4>
    <ul><li>Study</li><li>Travel</li><li>Education</li><li>Active</li><li>Course</li><li>Social</li><li>Natural</li><li>Online</li><li>English</li><li>Norwegian</li></ul>
  </div>
</footer>

<div class="bottom">© 2018 copyright Lunea | All rights reserved</div>

</body>
</html>
```